Book Cover (Front and Rear) for E book called Knotty Quarter

Create book cover front and rear book cover for e book called Knotty quarter. Knotty Quarter is a book of 99 puzzles made up of Sudoku, word scrambles, word searches, cross words, mine finder.

Looking for a fairly simple cover similar to the attached 2 designs. Must mention title of book (Knotty quarter) as well as making it clear that it is a book of puzzles and my name as the author (Carl Whitmore). Rear cover basically same colour as front however just plain.

```html
<!DOCTYPE html>
<html lang="en">
<head>
<meta charset="utf-8">
<title>Knotty Quarter — Front and Rear Cover</title>
<link rel="stylesheet" href="https://fonts.googleapis.com/css2?family=Montserrat:wght@500;600;700&display=swap">
<style>
  :root {
    --cover-green: #32c472;
    --spine-green: #2db868;
    --ink: #111111;
    --paper: #ffffff;
    --art-light: #f4f5f8;
    --art-mid: #d7dbe8;
    --ray-yellow: #f5e96a;
  }
  * { margin: 0; padding: 0; box-sizing: border-box; }
  html, body {
    width: 1200px;
    height: 1200px;
    overflow: hidden;
    background: var(--paper);
  }
  .stage {
    position: relative;
    width: 1200px;
    height: 1200px;
    display: flex;
    align-items: center;
    justify-content: center;
    gap: 60px;
  }
  .cover {
    position: relative;
    width: 390px;
    height: 600px;
    background: var(--cover-green);
    font-family: "Montserrat", sans-serif;
    color: var(--paper);
  }
  .front-cover {
    display: flex;
    flex-direction: column;
    align-items: center;
    padding-top: 36px;
  }
  .title-top {
    font-weight: 700;
    font-size: 52px;
    letter-spacing: 2px;
    line-height: 1;
  }
  .title-bottom {
    margin-top: 10px;
    font-weight: 500;
    font-size: 34px;
    letter-spacing: 12px;
    padding-left: 12px;
    line-height: 1;
  }
  .puzzle-list {
    list-style: none;
    margin-top: 16px;
    width: 300px;
    display: flex;
    flex-wrap: wrap;
    justify-content: center;
    gap: 2px 10px;
    color: var(--ink);
    font-weight: 500;
    font-size: 15px;
    line-height: 1.35;
  }
  .puzzle-list li {
    display: flex;
    align-items: center;
    gap: 5px;
  }
  .puzzle-list li::before {
    content: "";
    width: 4px;
    height: 4px;
    background: var(--paper);
  }
  .cover-art {
    margin-top: 28px;
    width: 210px;
    height: 210px;
    border-radius: 50%;
    background: radial-gradient(circle at 50% 50%, var(--art-light) 0%, var(--art-mid) 55%, var(--ray-yellow) 56%, var(--cover-green) 72%);
  }
  .author {
    position: absolute;
    bottom: 48px;
    left: 0;
    right: 0;
    text-align: center;
    color: var(--ink);
    font-weight: 600;
    font-size: 19px;
    letter-spacing: 6px;
  }
  .rear-cover {
    background: var(--cover-green);
  }
</style>
</head>
<body>
  <main class="stage">
    <section class="cover front-cover" aria-label="Front cover">
      <h1 class="book-title">
        <span class="title-top" style="display:block;text-align:center;">KNOTTY</span>
        <span class="title-bottom" style="display:block;text-align:center;">QUARTER</span>
      </h1>
      <ul class="puzzle-list">
        <li>SUDOKU</li>
        <li>WORD SCRAMBLES</li>
        <li>WORD SEARCHES</li>
        <li>CROSS WORDS</li>
        <li>MINE FINDER</li>
        <li>and more</li>
      </ul>
      <div class="cover-art" role="img" aria-label="Circular collage of crossword, sudoku and word search grids with yellow rays bursting around it"></div>
      <p class="author">CARL WHITMORE</p>
    </section>
    <section class="cover rear-cover" aria-label="Rear cover"></section>
  </main>
</body>
</html>
```